"Cork Hollow Excursions" is a top notch Santa Barbara County Wine Tour company.

We provide scenic, boutique and custom wine tours. I need the card to be clean and classy. I will provide our logo. I would like the logo to cover the back side of the card as an option and would like to see a couple color options other then our signature green and gold. I would like to see some creative options and let the designers come up with options.
I need cards for myself and my team. The final design should communicate "An authentic and boutique wine tour experience"
Please use my website for reference www.corkhollowexcursions.com

Target Market(s)

We have a wide range of clients from millennials to baby boomers

Industry/Entity Type

Tour

Contact Information for Business Card

Contact info:
Dale Munford
805-291-6384
info@corkhollowexcursions.com
corkhollowexcursions.com

Colors

Designer to choose colors to be used in the design.

Requirements
Must have
• my logo
Nice to have
• *I would like to have the backside side with the logo and the company statement
• "An authentic and boutique wine tour experience" as an option.
• *I would also like to see what the designers can create!
• *I would like to see an option that incorporates or social: snapgrid, rovia, route scout
Should not have
• I do not want it too busy.

```html
<!DOCTYPE html>
<html lang="en">
<head>
<meta charset="utf-8">
<title>Cork Hollow Excursions – Business Card</title>
<link rel="stylesheet" href="https://fonts.googleapis.com/css2?family=Cinzel:wght@400;600;700&family=Open+Sans:wght@400&display=swap">
<style>
  :root {
    --backdrop: #6a6a6a;
    --card-white: #ffffff;
    --brand-green: #1f6a3c;
    --brand-green-deep: #0d4a2b;
    --brand-green-mid: #17603a;
    --text-grey: #3a3a3a;
    --rule-grey: #9a9a9a;
    --on-green: #ffffff;
  }
  * { margin: 0; padding: 0; box-sizing: border-box; }
  html, body { width: 1200px; height: 1008px; overflow: hidden; }
  body { background: var(--backdrop); position: relative; font-family: "Open Sans", Arial, sans-serif; }

  .card { position: absolute; left: 318px; width: 560px; height: 320px; overflow: hidden; }

  /* Front */
  .card-front { top: 166px; background: var(--card-white); }
  .brand-mark {
    position: absolute; left: 40px; top: 160px; transform: translateY(-50%);
    width: 212px; display: flex; flex-direction: column; align-items: center; gap: 10px;
  }
  .brand-dot { width: 14px; height: 14px; border-radius: 50%; background: var(--brand-green); }
  .brand-name {
    font-family: "Cinzel", Georgia, serif; font-weight: 600; font-size: 20px; line-height: 1.2;
    color: var(--brand-green); text-align: center; letter-spacing: 0.5px;
  }
  .divider { position: absolute; left: 279px; top: 98px; width: 1px; height: 126px; background: var(--rule-grey); }
  .contact-block { position: absolute; left: 294px; top: 104px; }
  .person-name {
    font-family: "Cinzel", Georgia, serif; font-weight: 700; font-size: 17px;
    color: var(--brand-green); letter-spacing: 0.3px; line-height: 1.2;
  }
  .person-title { font-size: 14.5px; color: var(--text-grey); margin-top: 2px; }
  .contact-list { list-style: none; margin-top: 14px; }
  .contact-list li {
    display: flex; align-items: center; gap: 6px; font-size: 14px; color: var(--text-grey);
    line-height: 20.5px;
  }
  .contact-list svg { width: 14px; height: 14px; flex: none; }

  /* Back */
  .card-back {
    top: 527px;
    background: radial-gradient(ellipse at 55% 10%, #1c7043 0%, var(--brand-green-mid) 40%, var(--brand-green-deep) 100%);
    color: var(--on-green); text-align: center;
  }
  .vineyard-scene {
    position: absolute; left: 0; top: 0; width: 100%; height: 100%;
    background:
      radial-gradient(ellipse at 14% 30%, rgba(120,190,140,0.22) 0%, rgba(120,190,140,0) 45%),
      linear-gradient(180deg, rgba(0,0,0,0) 55%, rgba(40,120,70,0.35) 75%, rgba(10,60,35,0.3) 100%);
  }
  .statement-band { position: absolute; left: 0; bottom: 0; width: 100%; height: 50px; background: rgba(8,60,34,0.35); }
  .back-brand {
    position: absolute; left: 0; right: 0; top: 128px;
    font-family: "Cinzel", Georgia, serif; font-weight: 600; font-size: 34px; line-height: 1.1; letter-spacing: 1px;
  }
  .social-row {
    position: absolute; left: 0; right: 0; top: 236px; display: flex; justify-content: center; gap: 14px;
    font-family: "Cinzel", Georgia, serif; font-weight: 400; font-size: 10px; letter-spacing: 0.5px;
  }
  .tagline {
    position: absolute; left: 0; right: 0; top: 267px;
    font-family: "Cinzel", Georgia, serif; font-weight: 400; font-size: 13.5px; letter-spacing: 0.4px;
  }
</style>
</head>
<body>
  <section class="card card-front" aria-label="Business card front">
    <div class="brand-mark">
      <span class="brand-dot"></span>
      <div class="brand-name">Cork Hollow Excursions</div>
    </div>
    <div class="divider"></div>
    <div class="contact-block">
      <div class="person-name">DALE MUNFORD</div>
      <div class="person-title">Your Title</div>
      <ul class="contact-list">
        <li>
          <svg viewBox="0 0 14 14" aria-hidden="true"><circle cx="7" cy="7" r="7" fill="#1f6a3c"/><rect x="3.5" y="4.5" width="7" height="5" fill="none" stroke="#fff" stroke-width="1"/><path d="M3.5 4.5 L7 7.4 L10.5 4.5" fill="none" stroke="#fff" stroke-width="1"/></svg>
          info@corkhollowexcursions.com
        </li>
        <li>
          <svg viewBox="0 0 14 14" aria-hidden="true"><circle cx="7" cy="7" r="7" fill="#1f6a3c"/><path d="M3.5 6 Q7 3.5 10.5 6 L9.5 7 L8.5 6.3 L5.5 6.3 L4.5 7 Z" fill="#fff"/><rect x="4.5" y="7.3" width="5" height="3" rx="0.6" fill="#fff"/></svg>
          805-291-6384
        </li>
        <li>
          <svg viewBox="0 0 14 14" aria-hidden="true"><circle cx="7" cy="7" r="7" fill="#1f6a3c"/><circle cx="7" cy="7" r="3.8" fill="none" stroke="#fff" stroke-width="0.9"/><ellipse cx="7" cy="7" rx="1.6" ry="3.8" fill="none" stroke="#fff" stroke-width="0.8"/><line x1="3.2" y1="7" x2="10.8" y2="7" stroke="#fff" stroke-width="0.8"/></svg>
          corkhollowexcursions.com
        </li>
      </ul>
    </div>
  </section>

  <section class="card card-back" aria-label="Business card back">
    <div class="vineyard-scene" role="img" aria-label="Faint sunburst rising over mountains and vineyard rows"></div>
    <div class="statement-band"></div>
    <div class="back-brand">Cork Hollow Excursions</div>
    <div class="social-row"><span>snapgrid</span><span>rovia</span><span>route scout</span></div>
    <div class="tagline">AN AUTHENTIC AND BOUTIQUE WINE TOUR EXPERIENCE</div>
  </section>
</body>
</html>
```